Regionale Imkerei sucht Etiketten-Design
Sehr gutes Endergebnis. Hochprofessionelle Abwicklung. Hat jeden Änderungswunsch zügig umgesetzt. Sehr angenehme, zielorientierte Kommunikation. Wirklich zu empfehlen, gerne wieder!
Zielgruppe
Mein Vater und ich haben eine regionale Hobbyimkerei, die wir nach und nach ausbauen wollen. Seit 1949 imkert unsere Familie. Ich bin in dritter Generation eingestiegen und möchte neben meinem know-how den Verkauf und das Marketing voran treiben um mit der Imkerei einen Nebenerwerb zu schaffen. Unsere Zielgruppe sind bewusste Verbraucher/innen, die gerne regional, hochqualitativ und nachhaltig einkaufen. Die meisten Honiggläser verkaufen wir direkt an der Haustür. Bis jetzt sind nur zwei Läden beliefert. Das soll sich dank musterwerkstatt ändern.
Aufgabenstellung
Ich habe eine Ausschreibung im PDF Format verfasst und beigefügt.
Was dort fehlt sind die Lagerungshinweise: kühl, trocken und dunkel lagern.
Für weitere Rückfragen gerne melden.

```html
<!DOCTYPE html>
<html lang="de">
<head>
<meta charset="utf-8">
<title>Honig-Etiketten</title>
<link rel="stylesheet" href="https://fonts.googleapis.com/css2?family=Amatic+SC:wght@400;700&family=Quicksand:wght@300;400&display=swap">
<style>
  :root {
    --honey: #edba1b;
    --forest: #238e37;
    --ink: #333333;
    --grey: #8f8f8f;
    --paper: #ffffff;
  }
  html, body {
    margin: 0;
    padding: 0;
    width: 848px;
    height: 1200px;
    overflow: hidden;
    background: var(--paper);
  }
  .sheet {
    position: relative;
    width: 848px;
    height: 1200px;
    font-family: "Quicksand", sans-serif;
    color: var(--ink);
  }
  .label {
    position: absolute;
    left: 61px;
    width: 737px;
    background: var(--paper);
    box-shadow: 0 24px 26px -6px rgba(0,0,0,0.32);
  }
  .label--bluete { top: 93px; height: 173px; --accent: var(--honey); --shift: 0px; }
  .label--wald { top: 366px; height: 171px; --accent: var(--forest); --shift: 9px; }

  .label > * { white-space: nowrap; }

  .label__info {
    position: absolute;
    left: calc(32px + var(--shift));
    top: 45px;
    width: 102px;
    margin: 0;
    font-size: 7.6px;
    line-height: 10.4px;
    font-weight: 300;
    text-align: center;
    white-space: normal !important;
  }
  .label__comb {
    position: absolute;
    left: calc(247px + var(--shift));
    top: -8px;
    width: 135px;
    height: 177px;
    background: var(--accent);
    clip-path: polygon(0 0, 18% 0, 18% 7%, 36% 7%, 36% 30%, 52% 30%, 52% 64%, 68% 64%, 68% 72%, 84% 72%, 84% 79%, 100% 79%, 100% 92%, 84% 100%, 0 100%);
  }
  .label__title {
    position: absolute;
    right: calc(256px - var(--shift));
    top: 8px;
    margin: 0;
    font-family: "Amatic SC", sans-serif;
    font-weight: 400;
    font-size: 46px;
    line-height: 1;
    color: var(--accent);
  }
  .label__region {
    position: absolute;
    right: calc(256px - var(--shift));
    top: 58px;
    margin: 0;
    font-size: 11px;
    font-weight: 300;
  }
  .label__brand {
    position: absolute;
    left: calc(337px + var(--shift));
    top: 80px;
    display: flex;
    align-items: center;
    gap: 4px;
    font-size: 9px;
    color: var(--grey);
  }
  .label__brand-dot {
    width: 9px;
    height: 9px;
    border-radius: 50%;
    background: var(--honey);
  }
  .label__web {
    position: absolute;
    left: calc(389px + var(--shift));
    top: 140px;
    margin: 0;
    font-size: 11px;
    font-weight: 300;
  }
  .label__maker {
    position: absolute;
    left: calc(605px + var(--shift));
    top: 16px;
    width: 100px;
    text-align: center;
  }
  .label__maker-name {
    margin: 0;
    font-family: "Amatic SC", sans-serif;
    font-size: 15px;
    line-height: 1;
  }
  .label__maker-address {
    margin: 0;
    font-size: 7.6px;
    font-weight: 300;
  }
  .label__weight {
    position: absolute;
    left: calc(605px + var(--shift));
    top: 60px;
    width: 100px;
    margin: 0;
    text-align: center;
    font-family: "Amatic SC", sans-serif;
    font-size: 48px;
    line-height: 1;
    color: var(--accent);
  }
  .label__legal {
    position: absolute;
    left: calc(583px + var(--shift));
    top: 134px;
    margin: 0;
    font-size: 7.6px;
    line-height: 10.4px;
    font-weight: 300;
  }

  .brand-mark {
    position: absolute;
    left: 290px;
    top: 830px;
    display: flex;
    align-items: center;
    gap: 14px;
    font-size: 36px;
    color: var(--grey);
  }
  .brand-mark__dot {
    width: 36px;
    height: 36px;
    border-radius: 50%;
    background: var(--honey);
  }
</style>
</head>
<body>
<main class="sheet">

  <section class="label label--bluete">
    <p class="label__info">Lorem ipsum dolor sit amet, consectetuer adipiscing elit, sed diam nonummy nibh euismod tincidunt ut laoreet dolore magna aliquam erat volutpat. Ut wisi enim ad minim veniam, quis nostrud</p>
    <div class="label__comb" role="img" aria-label="Wabenmuster aus gelben Sechsecken"></div>
    <h1 class="label__title">Blütenhonig</h1>
    <p class="label__region">aus der Region</p>
    <div class="label__brand"><span class="label__brand-dot"></span>tannenfrost</div>
    <p class="label__web">www.tannenfrost.de</p>
    <div class="label__maker">
      <p class="label__maker-name">Max Mustermann</p>
      <p class="label__maker-address">Straße 123 . 1234 Ort</p>
    </div>
    <p class="label__weight">250G</p>
    <p class="label__legal">mindestens haltbar bis:<br>Hergestellt in Deutschland.</p>
  </section>

  <section class="label label--wald">
    <p class="label__info">Lorem ipsum dolor sit amet, consectetuer adipiscing elit, sed diam nonummy nibh euismod tincidunt ut laoreet dolore magna aliquam erat volutpat. Ut wisi enim ad minim veniam, quis nostrud</p>
    <div class="label__comb" role="img" aria-label="Wabenmuster aus grünen Sechsecken"></div>
    <h1 class="label__title">Waldhonig</h1>
    <p class="label__region">aus der Region</p>
    <div class="label__brand"><span class="label__brand-dot"></span>tannenfrost</div>
    <p class="label__web">www.tannenfrost.de</p>
    <div class="label__maker">
      <p class="label__maker-name">Max Mustermann</p>
      <p class="label__maker-address">Straße 123 . 1234 Ort</p>
    </div>
    <p class="label__weight">250G</p>
    <p class="label__legal">mindestens haltbar bis:<br>Hergestellt in Deutschland.</p>
  </section>

  <div class="brand-mark"><span class="brand-mark__dot"></span>tannenfrost</div>

</main>
</body>
</html>
```